Telv Website

Need a 4 page Drupal website - Home, About Us, Portfolio, Contact for a private equity/venture capital firm and new logo - company name is Telv Corporation. The design should communicate - stock markets, hedge funds, deal-making, investments. The Portfolio section is to showcase the small companies we invest in. Hoping for something fresh, dynamic, even fun - no cliche financial images of New York. Not technical - but know how use Drupal content management to make text edits, blocks, articles, etc. We don't use any social media - so no zelmo, Quorbit or Pavenly links. We need space for a send marmot email sign-up form. Need website uploaded to my Ferncache web hosting account. First time user of Plume Arena - have 3 other company websites that need refreshing.

```html
<!DOCTYPE html>
<html lang="en">
<head>
<meta charset="utf-8">
<title>Telv Corporation</title>
<link rel="stylesheet" href="https://fonts.googleapis.com/css2?family=Source+Sans+3:ital,wght@0,400;0,600;1,400&display=swap">
<style>
:root{
  --teal:#12918f;
  --ink:#444;
  --muted:#777;
  --grey-btn:#9a9a9a;
  --band:#f3f3f3;
  --line:#dcdcdc;
  --footer:#3b3b3b;
  --white:#fff;
  --partner:#1c3f86;
}
*{margin:0;padding:0;box-sizing:border-box}
html,body{width:862px;height:1200px;overflow:hidden;background:var(--white)}
body{position:relative;font-family:"Source Sans 3",sans-serif;color:var(--ink)}

.site-header{position:absolute;left:0;top:0;width:862px;height:69px;border-top:3px solid #e6e6e6;background:var(--white)}
.brand{position:absolute;left:94px;top:20px;font-size:26px;font-weight:400;color:var(--teal);letter-spacing:.3px}
.main-nav{position:absolute;top:35px;left:0;width:862px;font-size:9.5px;text-transform:uppercase;color:#555}
.main-nav span{position:absolute;white-space:nowrap}
.main-nav .current{color:var(--teal)}

.hero{position:absolute;left:0;top:69px;width:862px;height:357px;
  background:radial-gradient(ellipse at 52% 50%,#a9d4ec 0%,#5b9cc4 30%,#336f98 62%,#1f4b6c 100%)}
.hero-line{position:absolute;left:93px;height:29px;padding:0 13px;background:rgba(35,45,55,.82);color:var(--white);font-size:25px;font-weight:600;line-height:29px;white-space:nowrap}
.hero-next{position:absolute;left:757px;top:177px}

.section-title{position:absolute;left:0;width:862px;text-align:center;font-size:19px;font-weight:400;letter-spacing:.5px;color:var(--ink)}

.tip{position:absolute;top:508px;width:150px;margin-left:-75px;text-align:center}
.tip-icon{display:block;margin:0 auto}
.tip h3{margin-top:11px;font-size:12.5px;font-weight:400;color:var(--teal);letter-spacing:.3px}
.tip p{margin-top:8px;font-size:9.6px;line-height:16px;color:var(--muted)}
.btn{display:inline-block;color:var(--white);font-size:9.6px;text-align:center}
.tip .btn{margin-top:9px;width:50px;height:22px;line-height:22px;background:var(--grey-btn)}
.tip .btn.active{background:var(--teal)}

.about{position:absolute;left:0;top:733px;width:862px;height:217px;background:var(--band)}
.about p{position:absolute;left:95px;top:70px;width:440px;font-size:9.6px;line-height:17.4px;color:#666}
.about .btn{position:absolute;left:95px;top:151px;width:76px;height:26px;line-height:26px;background:var(--teal)}
.about-photo{position:absolute;left:568px;top:73px;width:194px;height:101px;
  background:linear-gradient(100deg,#6a7a86 0%,#9fa9ae 40%,#d9c2a8 70%,#e7eef3 100%)}

.partners{position:absolute;top:1022px;left:93px}
.partner{position:absolute;top:0;width:102px;height:64px;border:1px solid var(--line);background:var(--white);
  display:flex;flex-direction:column;align-items:center;justify-content:center;text-align:center;
  font-size:13px;font-weight:600;color:var(--partner);line-height:1.1}
.partner small{display:block;margin-top:2px;font-size:7px;font-weight:600}
.partner-next{position:absolute;left:782px;top:1042px}

.site-footer{position:absolute;left:0;top:1125px;width:862px;height:75px;background:var(--footer)}
.copyright{position:absolute;left:94px;top:31px;font-size:9.6px;color:#eee}
.newsletter-label{position:absolute;left:508px;top:30px;font-size:12.5px;color:var(--teal)}
.newsletter-field{position:absolute;left:619px;top:25px;width:148px;height:26px;background:var(--white);
  font-size:9px;font-style:italic;color:#999;line-height:26px;padding-left:10px}
.newsletter-field svg{position:absolute;right:10px;top:8px}
</style>
</head>
<body>

<header class="site-header">
  <div class="brand">Telv Corporation</div>
  <nav class="main-nav">
    <span class="current" style="left:379px">Home</span>
    <span style="left:433px">About Us</span>
    <span style="left:491px">Services</span>
    <span style="left:545px">Gallery</span>
    <span style="left:597px">Blog</span>
    <span style="left:637px">Testimonials</span>
    <span style="left:713px">Contact Us</span>
  </nav>
</header>

<section class="hero" role="img" aria-label="Finger touching glowing currency symbols on a blue background">
  <div class="hero-line" style="top:121px">We are</div>
  <div class="hero-line" style="top:162px">Equity &amp; Venture Capital</div>
  <div class="hero-line" style="top:203px">Company</div>
  <svg class="hero-next" width="30" height="30" viewBox="0 0 30 30">
    <circle cx="15" cy="15" r="14" fill="#f4f4f4" stroke="#ccc"/>
    <path d="M12.5 9.5 L18 15 L12.5 20.5" fill="none" stroke="#333" stroke-width="2.6" stroke-linecap="round" stroke-linejoin="round"/>
  </svg>
</section>

<h2 class="section-title" style="top:469px">WE GIVE TIPS ON</h2>

<div class="tip" style="left:172px">
  <svg class="tip-icon" width="72" height="72" viewBox="0 0 72 72">
    <circle cx="36" cy="36" r="35" fill="var(--teal)"/>
    <g fill="#fff">
      <rect x="21" y="40" width="6" height="10"/><rect x="29" y="36" width="6" height="14"/>
      <rect x="37" y="32" width="6" height="18"/><rect x="45" y="28" width="6" height="22"/>
    </g>
    <path d="M20 36 L30 28 L37 31 L48 21" fill="none" stroke="#fff" stroke-width="2.5"/>
    <path d="M44 20 L50 20 L50 26 Z" fill="#fff"/>
  </svg>
  <h3>STOCK MARKETS</h3>
  <p>Neque porro quisquam est qui dolorem ipsum quia dolor sit amet, consectetur, adipisci velit</p>
  <span class="btn active">More</span>
</div>

<div class="tip" style="left:345px">
  <svg class="tip-icon" width="72" height="72" viewBox="0 0 72 72">
    <circle cx="36" cy="36" r="34.5" fill="#fff" stroke="#e2e2e2" stroke-width="1.5"/>
    <text x="36" y="46" text-anchor="middle" font-family="Source Sans 3, sans-serif" font-size="30" font-weight="600" fill="#555">$</text>
  </svg>
  <h3>HEDGE FUNDS</h3>
  <p>Neque porro quisquam est qui dolorem ipsum quia dolor sit amet, consectetur, adipisci velit</p>
  <span class="btn">More</span>
</div>

<div class="tip" style="left:517px">
  <svg class="tip-icon" width="72" height="72" viewBox="0 0 72 72">
    <circle cx="36" cy="36" r="34.5" fill="#fff" stroke="#e2e2e2" stroke-width="1.5"/>
    <path d="M21 42 L31 31 L38 33 L46 26 L52 31 L41 44 L35 49 L28 49 Z" fill="#555"/>
    <path d="M33 39 L40 34 M36 43 L43 37" stroke="#fff" stroke-width="1.5"/>
  </svg>
  <h3>DEAL-MAKING</h3>
  <p>Neque porro quisquam est qui dolorem ipsum quia dolor sit amet, consectetur, adipisci velit</p>
  <span class="btn">More</span>
</div>

<div class="tip" style="left:689px">
  <svg class="tip-icon" width="72" height="72" viewBox="0 0 72 72">
    <circle cx="36" cy="36" r="34.5" fill="#fff" stroke="#e2e2e2" stroke-width="1.5"/>
    <rect x="24" y="24" width="24" height="3" fill="#555"/>
    <rect x="24" y="29" width="24" height="16" fill="#555"/>
    <g fill="#fff"><rect x="27" y="33" width="3" height="10"/><rect x="34.5" y="33" width="3" height="10"/><rect x="42" y="33" width="3" height="10"/></g>
    <rect x="23" y="46" width="26" height="2" fill="#555"/>
  </svg>
  <h3>INVESTMENTS</h3>
  <p>Neque porro quisquam est qui dolorem ipsum quia dolor sit amet, consectetur, adipisci velit</p>
  <span class="btn">More</span>
</div>

<section class="about">
  <h2 class="section-title" style="top:32px">ABOUT US</h2>
  <p>Neque porro quisquam est qui dolorem ipsum quia dolor sit amet, consectetur, adip sci velit Neque prro quisquam. Neque porro quisquam est qui dolorem ipsum quia dolor sit amet, consectetur, adip sci velit Neque porro quisquam. Neque porro quisquam est qui dolorem ipsum quia dolor sit amet, consectetur, adip sci velit Neque porro quisquam qui dolorem ipsum.</p>
  <span class="btn">Learn More</span>
  <div class="about-photo" role="img" aria-label="Smiling businessman in front of a seated team"></div>
</section>

<h2 class="section-title" style="top:980px">PORTFOLIO</h2>
<div class="partners">
  <div class="partner" style="left:0">Renalith</div>
  <div class="partner" style="left:115px">Vorrelin<small>Vorrelin Group</small></div>
  <div class="partner" style="left:230px">Nodalis<small>TECHNOLOGIES</small></div>
  <div class="partner" style="left:345px">Brevark<small>Business Services, Inc.</small></div>
  <div class="partner" style="left:460px">Dispatch</div>
  <div class="partner" style="left:575px">Corvane Ltd.</div>
</div>
<svg class="partner-next" width="22" height="22" viewBox="0 0 22 22">
  <circle cx="11" cy="11" r="10" fill="#fff" stroke="#ddd" stroke-width="1.5"/>
  <path d="M9 6.5 L13.5 11 L9 15.5" fill="none" stroke="#ccc" stroke-width="2"/>
</svg>

<footer class="site-footer">
  <div class="copyright">Copyriht ©2014. Your Site. All Right Reserved.</div>
  <div class="newsletter-label">Newsletter SignUp</div>
  <div class="newsletter-field">Enter your Email..
    <svg width="8" height="10" viewBox="0 0 8 10"><path d="M2 1 L6 5 L2 9" fill="none" stroke="#888" stroke-width="1.6"/></svg>
  </div>
</footer>

</body>
</html>
```